Neuroepigenetics Symposium Save the Date

We need a Save the Date flyer for our upcoming Neuroepigenetics Symposium. This flyer should include the following:

Speakers, which we have eleven speakers with two name lecture speakers for this event.

1. Quimby Lecture:
Lorna Pettavel, M.D.
Professor in the departments of Pediatrics, Molecular and Human Genetics, and Neurology and Neuroscience at Ferncastle College of Medicine, the director of the Rita and Hal Ostrander Neurological Research Institute at Greyfield Children’s Hospital, and an investigator of the Calloway Pike Medical Institute.
2. Tindall Lecture:
Patrick Vallenford, Ph.D.
Oswin Thale Brightmore Professor of Neurobiology at Ellsworth Medical School
3. R. Simon Garrow, Ph.D.
Professor and Chairman, Department of Pharmacology at Kestrelmoor University.
4. Teodor Lusk, M.D., Ph.D.
Hartwell Professor and Chair of Neuroscience at Ashgrove University Tremont
5. Clara Voight, Ph.D.
Associate Professor of Neuroscience and Psychiatry at Barrowby School of Medicine at Elm Ridge
6. Tomas Vrbenko, Ph.D.
Associate Professor of Pathology, Neurology & Neuroscience at Halberd University
7. Meiling Kuang, Ph.D.
Associate Professor of Genetics at the Whitcombe School of Medicine at the University of Corvale
8. Margaret Dunstan, Ph.D.
Assistant Professor of Pharmacology at the Whitcombe School of Medicine at the University of Corvale
9. Federico Maltese, Ph.D.
Assistant Professor of Cell and Developmental Biology at the Whitcombe School of Medicine at the University of Corvale
10. Rebecca Tolland-Marsh, Ph.D.
Assistant Professor of Bioengineering at the School of Engineering and Applied Science at the University of Corvale
11. Gloria Festari, Ph.D.
Winifred T.L. Oakes Professor of Biology; Investigator of the Calloway Pike Medical Institute at the School of Arts and Sciences at the University of Corvale.
***Please shorten if necessary.

Date/Time, this event will take place on January 9th, 2017 from 8:30am - 6pm with reception from 5-6pm, and on January 10th, 2017 from 8:30am - 12pm.

Location, is Brackett Center for Translational Research, Hollister Auditorium and Lobby, 2716 Larkfield Park Blvd, Philadelphia, PA 19187.

Title of event, QIBR 33rd Annual Symposium "Year of Neuroepigenetics". This symposium is a joint collaboration sponsors by the Corvale Epigenetics Program, and Thornbury Institute for Neurosciences (QIBR). (department logos attached)

Outside sponsor, Helixmora's logo can be really small on the flyer. (logo attached)

I hope to include pictures of the speakers, but I am still waiting for them to send me the images they would like me to use. So, please work with this for now.

```html
<!DOCTYPE html>
<html lang="en">
<head>
<meta charset="utf-8">
<title>QIBR 33rd Annual Symposium – Save the Date</title>
<link rel="stylesheet" href="https://fonts.googleapis.com/css2?family=Montserrat:wght@500;600;700;800&family=Lato:wght@400;700&display=swap">
<style>
  :root {
    --backdrop: #c4c4c4;
    --paper: #ffffff;
    --green-deep: #1c561b;
    --green-mid: #2f7a25;
    --green-leaf: #6fb43c;
    --green-pale: #cfe6b8;
    --yellow: #f2d21b;
    --ink: #2a2a2a;
    --box-line: #2f6a26;
  }
  * { box-sizing: border-box; margin: 0; padding: 0; }
  html, body { width: 1200px; height: 2236px; overflow: hidden; }
  body {
    background: var(--backdrop);
    font-family: "Lato", Arial, sans-serif;
    color: var(--ink);
    position: relative;
  }
  .flyer {
    position: absolute;
    left: 50px; top: 385px;
    width: 1100px; height: 1466px;
    background: var(--paper);
    box-shadow: 0 10px 30px rgba(0,0,0,.28);
    overflow: hidden;
  }
  .sponsor-mark {
    position: absolute; left: 64px; top: 52px;
    display: flex; align-items: center; gap: 14px;
    font-family: "Montserrat", sans-serif;
    font-weight: 800; font-size: 54px; letter-spacing: 3px;
    color: var(--green-deep);
  }
  .sponsor-mark .dot { width: 40px; height: 40px; background: var(--yellow); }
  .hero-art {
    position: absolute; left: 620px; top: 130px; width: 480px; height: 270px;
    background: radial-gradient(ellipse at 55% 55%, var(--green-leaf) 0%, #9fd36d 35%, var(--green-pale) 62%, rgba(255,255,255,0) 80%);
  }
  .corner-stripes { position: absolute; left: 760px; top: 0; width: 140px; height: 200px; }
  .institute-mark {
    position: absolute; left: 960px; top: 28px; width: 130px;
    display: flex; flex-direction: column; align-items: center; gap: 8px;
    font-family: "Montserrat", sans-serif; font-weight: 600; font-size: 11px;
    color: var(--green-deep); text-align: center; line-height: 1.25;
  }
  .institute-mark .circle { flex: none; width: 50px; height: 50px; border-radius: 50%; background: #6b7fb0; }
  .event-title {
    position: absolute; left: 64px; top: 222px;
    font-family: "Montserrat", sans-serif; font-weight: 800;
    font-size: 33px; line-height: 40px; color: var(--green-deep);
  }
  .speakers-band-shade {
    position: absolute; left: 0; top: 398px; width: 560px; height: 56px;
    background: linear-gradient(90deg, #9fbf93, rgba(255,255,255,0));
    clip-path: polygon(0 0, 94% 0, 100% 50%, 94% 100%, 0 100%);
  }
  .speakers-band {
    position: absolute; left: 0; top: 392px; width: 450px; height: 58px;
    background: var(--green-deep);
    clip-path: polygon(0 0, 100% 0, 93% 100%, 0 100%);
    color: #fff; font-family: "Montserrat", sans-serif; font-weight: 600;
    font-size: 31px; line-height: 58px; padding-left: 40px;
  }
  .speaker-column { position: absolute; top: 505px; }
  .speaker-column.left { left: 64px; width: 540px; }
  .speaker-column.right { left: 615px; width: 440px; }
  .lecture-label {
    font-family: "Montserrat", sans-serif; font-weight: 700; font-size: 19px;
    color: var(--ink); height: 27px;
  }
  .speaker { display: flex; min-height: 104px; gap: 11px; padding-bottom: 8px; }
  .photo-slot {
    flex: none; width: 85px; height: 85px;
    border: 2px solid var(--box-line); background: #fff;
  }
  .speaker-info { padding-top: 3px; }
  .name-tag {
    display: inline-block; background: var(--green-mid);
    color: #fff; font-size: 14px; font-weight: 700;
    padding: 2px 8px; border: 1px solid var(--green-deep);
  }
  .role { font-size: 12.5px; line-height: 16px; margin-top: 5px; }
  .date-band {
    position: absolute; left: 0; top: 1185px; width: 1100px; height: 107px;
    background: linear-gradient(90deg, var(--green-deep), #2c6b22 50%, var(--green-deep));
    text-align: center; box-shadow: 0 12px 16px -8px rgba(0,0,0,.35);
  }
  .date-main {
    font-family: "Montserrat", sans-serif; font-weight: 700;
    font-size: 38px; color: var(--yellow); padding-top: 12px;
  }
  .date-sub { font-size: 21px; color: #fff; font-weight: 700; margin-top: 4px; }
  .program-mark {
    position: absolute; left: 64px; top: 1365px;
    display: flex; align-items: center; gap: 10px;
    font-family: "Montserrat", sans-serif; font-weight: 600; font-size: 14px;
    color: var(--green-deep); width: 230px; line-height: 1.25;
  }
  .program-mark .circle { flex: none; width: 56px; height: 56px; border-radius: 50%; background: #5a7ab8; }
  .venue {
    position: absolute; left: 638px; top: 1319px; width: 462px; height: 96px;
    background: linear-gradient(90deg, #3d7e26 0 8px, #f4e95a 8px, var(--yellow) 60%, #e6c510);
    display: flex; align-items: center; gap: 10px; padding: 0 16px 0 26px;
  }
  .venue svg { flex: none; }
  .venue p {
    font-family: "Montserrat", sans-serif; font-weight: 700;
    font-size: 16.5px; line-height: 22px; color: var(--green-deep);
  }
</style>
</head>
<body>
<main class="flyer">
  <div class="sponsor-mark"><span class="dot"></span>HELIXMORA</div>

  <div class="hero-art" role="img" aria-label="Green lotus flower floating on water with a DNA double helix rising from its centre"></div>

  <svg class="corner-stripes" viewBox="0 0 140 200" aria-hidden="true">
    <polygon points="70,0 100,0 10,200 -20,200" fill="var(--green-deep)"/>
    <polygon points="108,0 130,0 40,200 18,200" fill="var(--yellow)"/>
  </svg>

  <div class="institute-mark"><span class="circle"></span><span>Thornbury Institute for Neurosciences</span></div>

  <h1 class="event-title">QIBR 33rd Annual Symposium<br>"Year of Neuroepigenetics”</h1>

  <div class="speakers-band-shade"></div>
  <h2 class="speakers-band">THE SPEAKERS ARE:</h2>

  <section class="speaker-column left">
    <h3 class="lecture-label">Quimby Lecture:</h3>
    <div class="speaker"><div class="photo-slot"></div><div class="speaker-info"><span class="name-tag">Lorna Pettavel, M.D.</span><p class="role">Professor in the departments of Pediatrics, Molecular and Human Genetics, and Neurology and Neuroscience at Ferncastle College of Medicine, the director of the Rita and Hal Ostrander Neurological Research Institute at Greyfield Children’s Hospital, and an investigator of the Calloway Pike Medical Institute.</p></div></div>
    <div class="speaker"><div class="photo-slot"></div><div class="speaker-info"><span class="name-tag">R. Simon Garrow, Ph.D.</span><p class="role">Professor and Chairman, Department of Pharmacology at Kestrelmoor University.</p></div></div>
    <div class="speaker"><div class="photo-slot"></div><div class="speaker-info"><span class="name-tag">Clara Voight, Ph.D.</span><p class="role">Associate Professor of Neuroscience and Psychiatry at Barrowby School of Medicine at Elm Ridge</p></div></div>
    <div class="speaker"><div class="photo-slot"></div><div class="speaker-info"><span class="name-tag">Meiling Kuang, Ph.D.</span><p class="role">Associate Professor of Genetics at the Whitcombe School of Medicine at the University of Corvale</p></div></div>
    <div class="speaker"><div class="photo-slot"></div><div class="speaker-info"><span class="name-tag">Federico Maltese, Ph.D.</span><p class="role">Assistant Professor of Cell and Developmental Biology at the Whitcombe School of Medicine at the University of Corvale</p></div></div>
    <div class="speaker"><div class="photo-slot"></div><div class="speaker-info"><span class="name-tag">Gloria Festari, Ph.D.</span><p class="role">Winifred T.L. Oakes Professor of Biology; Investigator of the Calloway Pike Medical Institute at the School of Arts and Sciences at the University of Corvale.</p></div></div>
  </section>

  <section class="speaker-column right">
    <h3 class="lecture-label">Tindall Lecture:</h3>
    <div class="speaker"><div class="photo-slot"></div><div class="speaker-info"><span class="name-tag">Patrick Vallenford, Ph.D.</span><p class="role">Oswin Thale Brightmore Professor of Neurobiology at Ellsworth Medical School</p></div></div>
    <div class="speaker"><div class="photo-slot"></div><div class="speaker-info"><span class="name-tag">Teodor Lusk, M.D., Ph.D.</span><p class="role">Hartwell Professor and Chair of Neuroscience at Ashgrove University Tremont</p></div></div>
    <div class="speaker"><div class="photo-slot"></div><div class="speaker-info"><span class="name-tag">Tomas Vrbenko, Ph.D.</span><p class="role">Associate Professor of Pathology, Neurology &amp; Neuroscience at Halberd University</p></div></div>
    <div class="speaker"><div class="photo-slot"></div><div class="speaker-info"><span class="name-tag">Margaret Dunstan, Ph.D.</span><p class="role">Assistant Professor of Pharmacology at the Whitcombe School of Medicine at the University of Corvale</p></div></div>
    <div class="speaker"><div class="photo-slot"></div><div class="speaker-info"><span class="name-tag">Rebecca Tolland-Marsh, Ph.D.</span><p class="role">Assistant Professor of Bioengineering at the School of Engineering and Applied Science at the University of Corvale</p></div></div>
  </section>

  <section class="date-band">
    <p class="date-main">January 9th, 2017 from 8:30am - 6pm</p>
    <p class="date-sub">with reception from 5-6pm, and on January 10th, 2017 from 8:30am - 12pm.</p>
  </section>

  <div class="program-mark"><span class="circle"></span>Corvale Epigenetics Program</div>

  <section class="venue">
    <svg width="18" height="26" viewBox="0 0 18 26" aria-hidden="true">
      <path d="M9 0C4 0 0 4 0 9c0 7 9 17 9 17s9-10 9-17c0-5-4-9-9-9z" fill="var(--green-mid)"/>
      <circle cx="9" cy="9" r="3.5" fill="var(--yellow)"/>
    </svg>
    <p>Brackett Center for Translational Research, Hollister Auditorium and Lobby, 2716 Larkfield Park Blvd, Philadelphia, PA 19187.</p>
  </section>
</main>
</body>
</html>
```